Letterhead and Email Signature Needed

We need a letterhead for a mortgage pre-approval letter, and we also need a standard letterhead template for a memo.
We would also like an email signature created. We have a logo that is white background and grey background. I'd like the grey background version incorporated ideally, but if you manage to use both on the pre-approval letter and memo, thatt would be great. For the email signature, I'd prefer the grey background be used.
I included a sample document to show what information needs to be in the file pre-approval letter. The design and logo of the sample letter can be ignored.
Target Market(s)
Mortgage customers
Industry/Entity Type
Mortgage/Finance
Colors
Designer to choose colors to be used in the design.
Look and feel
Each slider illustrates characteristics of the customer's brand and the style your logo design should communicate.

```html
<!DOCTYPE html>
<html lang="en">
<head>
<meta charset="utf-8">
<title>Harlow Lending – Conditional Approval Letter</title>
<link href="https://fonts.googleapis.com/css2?family=Poppins:ital,wght@0,300;0,400;0,500;0,600;1,400&display=swap" rel="stylesheet">
<style>
  :root {
    --ink: #111111;
    --black: #000000;
    --red: #ee1111;
    --white: #ffffff;
    --rule: #222222;
  }
  * { margin: 0; padding: 0; box-sizing: border-box; }
  html, body { width: 848px; height: 1200px; overflow: hidden; background: var(--white); }
  body { font-family: 'Poppins', sans-serif; color: var(--ink); }
  .letter { position: relative; width: 848px; height: 1200px; overflow: hidden; }
  .shapes { position: absolute; inset: 0; width: 848px; height: 1200px; }
  .abs { position: absolute; white-space: nowrap; }

  .brand-name { left: 66px; width: 182px; top: 16px; text-align: center; color: var(--white);
    font-size: 25px; font-weight: 500; letter-spacing: -0.3px; line-height: 27px; }

  .firm { right: 180px; text-align: right; font-size: 12.5px; font-weight: 600; line-height: 17px; top: 28px; }
  .firm-address { right: 180px; top: 70px; font-size: 10.8px; font-weight: 300; }
  .firm-license { right: 180px; top: 93px; font-size: 10.8px; font-weight: 300; }
  .contact { left: 689px; font-size: 10.8px; font-weight: 300; }

  .meta { left: 65px; font-size: 13px; font-weight: 600; }
  .intro { left: 65px; top: 296px; width: 532px; white-space: normal; font-size: 14px; font-weight: 300; line-height: 24px; }

  .label { left: 65px; font-size: 13px; font-weight: 600; }
  .value { left: 300px; font-size: 13px; font-weight: 600; }
  .lead { left: 65px; font-size: 15px; font-weight: 300; }

  .conditions { position: absolute; left: 109px; top: 743px; list-style: none; }
  .conditions li { position: relative; padding-left: 19px; height: 29px; font-size: 14.5px; font-weight: 500; line-height: 20px; }
  .conditions li::before { content: ""; position: absolute; left: 0; top: 6px; width: 9px; height: 9px;
    border: 1.6px solid var(--red); border-radius: 50%; }

  .regards { left: 65px; top: 867px; font-size: 15px; font-weight: 300; }
  .signature { position: absolute; left: 65px; top: 906px; width: 150px; height: 34px; background: linear-gradient(90deg, #e9e9e9, #f6f6f6); border-radius: 3px; }
  .signer { left: 65px; top: 947px; font-size: 15.5px; font-weight: 300; line-height: 19.5px; }

  .notice-title { left: 66px; top: 1080px; color: var(--red); font-size: 15.5px; font-style: italic; font-weight: 400; }
  .notice-body { left: 67px; top: 1112px; width: 726px; white-space: normal; color: var(--white); font-size: 10px; font-weight: 400; line-height: 14.2px; }
  .doc-code { right: 9px; top: 1180px; color: var(--white); font-size: 9px; font-weight: 600; letter-spacing: 0.5px; }
</style>
</head>
<body>
<main class="letter">
  <svg class="shapes" viewBox="0 0 848 1200" aria-hidden="true">
    <rect class="top-bar-red" x="0" y="0" width="676" height="9" fill="var(--red)"/>
    <rect class="top-bar-black" x="679" y="0" width="169" height="9" fill="var(--black)"/>
    <path class="brand-tab" d="M66 0 H248 V103 C228 110 200 110 165 102 S96 92 66 99 Z" fill="var(--black)"/>
    <line class="header-rule" x1="677" y1="27" x2="677" y2="110" stroke="var(--rule)" stroke-width="1"/>
    <path class="footer-wave" d="M0 1052 C120 1030 270 1028 430 1056 S750 1112 848 1063 L848 1200 L0 1200 Z" fill="var(--black)"/>
  </svg>

  <div class="abs brand-name">Harlow<br>Lending</div>

  <div class="abs firm">Harlow Lending<br>Daniel Harlow, CEO</div>
  <div class="abs firm-address">48 Bayview Plaza Dr Irvine, CA 92614</div>
  <div class="abs firm-license">DRE License: 01234567</div>

  <div class="abs contact" style="top:29px">949.555.0142 Main</div>
  <div class="abs contact" style="top:50px">www.harlowlending.com</div>
  <div class="abs contact" style="top:71px">dan@harlowlending.com</div>
  <div class="abs contact" style="top:93px">NMLS ID: 1048821</div>

  <div class="abs meta" style="top:154px">October 8, 2024</div>
  <div class="abs meta" style="top:186px">Re: Sample Client</div>
  <div class="abs meta" style="top:217px">Property address: TBD</div>
  <div class="abs meta" style="top:249px">Dear Sample,</div>

  <p class="abs intro">Congratulations! After reviewing your loan application, we have determined that your qualifications allow us to conditionally approve you for a loan subject to the conditions listed below. While continuing with the purchase of your new home, you may present this letter, or a copy thereof, as proof of your loan preapproval.</p>

  <div class="abs label" style="top:451px">Occupancy Type:</div>
  <div class="abs value" style="top:451px">PRIMARY</div>
  <div class="abs label" style="top:481px">Loan Type:</div>
  <div class="abs value" style="top:481px">CONVENTIONAL</div>

  <div class="abs lead" style="top:529px">This conditional approval is based on the following loan terms:</div>

  <div class="abs label" style="top:583px">Estimated Purchase Price:</div>
  <div class="abs value" style="top:583px">$1,020,000</div>
  <div class="abs label" style="top:612px">Loan Amount:</div>
  <div class="abs value" style="top:613px">$867,000</div>
  <div class="abs label" style="top:643px">Estimated Down Payment:</div>
  <div class="abs value" style="top:644px">$153,000</div>

  <div class="abs lead" style="top:691px">Please note that this conditional approval is subject to the following:</div>

  <ul class="conditions">
    <li>Acceptable property appraisal</li>
    <li>All Credit, Income &amp; Assets to remain unchanged</li>
    <li>Fully executed Real Estate contract</li>
  </ul>

  <div class="abs regards">Regards,</div>
  <div class="signature" role="img" aria-label="Handwritten signature of Daniel Harlow"></div>
  <div class="abs signer">Daniel Harlow<br>NMLS ID: 390115<br>DRE License ID: 0176342</div>

  <div class="abs notice-title">EQUAL CREDIT OPPORTUNITY ACT NOTICE</div>
  <p class="abs notice-body">The Federal Equal Credit Opportunity Act prohibits creditors from discriminating against credit applicants on the basis of race, color, religion, national origin, sex, marital status, age (provided that the applicant has the capacity to enter into a binding contract); or because all or part of the applicant's income derives from any public assistance program; or because the applicant has in good faith exercised any right under the Consumer Credit Protection Act. The Federal agency that administers compliance with this law concerning this creditor is the office of the Thrift Supervision, Post Office Box 4410, 200 Market Street, Suite 300, San Francisco, California 94105</p>
  <div class="abs doc-code">C44</div>
</main>
</body>
</html>
```